Marlowe Holdings LLC - Business Cards

Need the following information on the cards:

Name: Dean R Vossler
Title: Chief Executive Manager

Business address:
412 N Ridgeview Lane #118
Ashford Crossing, Oh 60412

Phone: (630) 555-0148 - Business
KPV FFL license number: 5-21-xxx-xx-xx-04519
Email: dean.vossler@marloweholdingsffl.com

Target Market(s)

Firearm owners

Industry/Entity Type

Firearms industry,

Contact Information for Business Card

Contact number, name and title, web page address, email, business address and kpv license number,

Requirements
Must have
• Name, title, business address, phone numbers, KPV license numbers, web page address and email address.
Nice to have
• Cellphone number,

```html
<!DOCTYPE html>
<html lang="en">
<head>
<meta charset="utf-8">
<title>Marlowe Holdings LLC – Business Cards</title>
<link rel="stylesheet" href="https://fonts.googleapis.com/css2?family=Open+Sans:wght@400;700&family=Fira+Sans:wght@400;600&display=swap">
<style>
  :root {
    --backdrop: #bab8bd;
    --paper: #ffffff;
    --navy: #1e2940;
    --red: #ff0009;
    --ink: #1e2940;
  }
  * { margin: 0; padding: 0; box-sizing: border-box; }
  html, body { width: 1200px; height: 750px; overflow: hidden; }
  body { background: var(--backdrop); position: relative; font-family: "Fira Sans", sans-serif; color: var(--ink); }

  .card { position: absolute; top: 215px; width: 503px; height: 295px; background: var(--paper); overflow: hidden; }
  .card--front { left: 64px; }
  .card--back { left: 644px; }

  .holder-name { position: absolute; left: 29px; top: 40px; font-family: "Open Sans", sans-serif; font-weight: 700; font-size: 21px; line-height: 1; color: var(--navy); }
  .holder-title { position: absolute; left: 30px; top: 64px; font-family: "Open Sans", sans-serif; font-size: 12.5px; color: var(--navy); }

  .contact-list { position: absolute; left: 30px; top: 103px; list-style: none; }
  .contact-item { display: flex; align-items: center; height: 29px; margin-bottom: 9.5px; }
  .contact-icon { width: 29px; height: 29px; flex: none; margin-right: 6px; }
  .contact-text { font-size: 10.5px; line-height: 12.3px; color: var(--ink); white-space: nowrap; }

  .brand { position: absolute; width: 200px; text-align: center; top: 42px; }
  .card--front .brand { left: 295px; }
  .card--back .brand { left: 152px; }
  .brand-mark { display: block; margin: 0 auto; width: 92px; height: 92px; }
  .brand-name { margin-top: 5px; font-family: "Fira Sans", sans-serif; font-weight: 600; font-size: 14px; line-height: 16px; color: var(--navy); }

  .card-art { position: absolute; left: 0; top: 0; }

  .back-url { position: absolute; left: 0; right: 0; top: 256px; text-align: center; font-size: 10px; color: var(--paper); letter-spacing: 0.1px; }
</style>
</head>
<body>

<section class="card card--front" aria-label="Business card front">
  <svg class="card-art" width="503" height="295" viewBox="0 0 503 295" aria-hidden="true">
    <rect class="accent-band" x="200" y="252" width="303" height="31" fill="var(--red)"/>
    <path class="navy-block" d="M0 235 H193 Q199 235 203 240 L250 295 H0 Z" fill="var(--navy)"/>
  </svg>

  <h1 class="holder-name">Dean R Vossler</h1>
  <p class="holder-title">Chief Executive Manager</p>

  <ul class="contact-list">
    <li class="contact-item">
      <svg class="contact-icon" viewBox="0 0 29 29" aria-hidden="true">
        <circle cx="14.5" cy="14.5" r="14.5" fill="var(--red)"/>
        <rect x="10" y="6.5" width="9" height="16" rx="1.6" fill="none" stroke="#fff" stroke-width="1.6"/>
        <line x1="10" y1="19.2" x2="19" y2="19.2" stroke="#fff" stroke-width="1.2"/>
        <circle cx="14.5" cy="20.9" r="0.7" fill="#fff"/>
      </svg>
      <p class="contact-text">(630) 555-0148 - Business<br>KPV FFL license number: 5-21-xxx-xx-xx-04519</p>
    </li>
    <li class="contact-item">
      <svg class="contact-icon" viewBox="0 0 29 29" aria-hidden="true">
        <circle cx="14.5" cy="14.5" r="14.5" fill="var(--red)"/>
        <g fill="none" stroke="#fff" stroke-width="1.7" transform="rotate(40 14.5 14.5)">
          <rect x="5.5" y="11.5" width="9" height="6" rx="3"/>
          <rect x="14.5" y="11.5" width="9" height="6" rx="3"/>
        </g>
      </svg>
      <p class="contact-text">dean.vossler@marloweholdingsffl.com<br>www.marloweholdingsffl.com</p>
    </li>
    <li class="contact-item">
      <svg class="contact-icon" viewBox="0 0 29 29" aria-hidden="true">
        <circle cx="14.5" cy="14.5" r="14.5" fill="var(--red)"/>
        <path d="M14.5 23 C10 17 9 14.8 9 12.5 A5.5 5.5 0 0 1 20 12.5 C20 14.8 19 17 14.5 23 Z" fill="#fff"/>
        <circle cx="14.5" cy="12.5" r="2.1" fill="var(--red)"/>
      </svg>
      <p class="contact-text">412 N Ridgeview Lane #118<br>Ashford Crossing, Oh 60412</p>
    </li>
  </ul>

  <div class="brand">
    <svg class="brand-mark" viewBox="0 0 92 92" aria-hidden="true">
      <circle cx="46" cy="46" r="40" fill="none" stroke="var(--red)" stroke-width="2"/>
    </svg>
    <p class="brand-name">Marlowe<br>Holdings LLC</p>
  </div>
</section>

<section class="card card--back" aria-label="Business card back">
  <svg class="card-art" width="503" height="295" viewBox="0 0 503 295" aria-hidden="true">
    <path class="navy-tab" d="M98 240 L104 232 Q107 229 113 229 H406 Q412 229 415 232 L421 240 Z" fill="var(--navy)"/>
    <rect class="accent-band" x="0" y="240" width="503" height="55" fill="var(--red)"/>
  </svg>

  <div class="brand">
    <svg class="brand-mark" viewBox="0 0 92 92" aria-hidden="true">
      <circle cx="46" cy="46" r="40" fill="none" stroke="var(--red)" stroke-width="2"/>
    </svg>
    <p class="brand-name">Marlowe<br>Holdings LLC</p>
  </div>

  <p class="back-url">www.marloweholdingsffl.com</p>
</section>

</body>
</html>
```